New ideas for home page of my website

I am looking for some inspiration for my website www.crafteddownriver.com
Most of the content will stay the same but I will be adding on the following new buttons Annual Expo and Awards
Any ideas on alternative layout act will be great. The most creative idea will get the opportunity to pitch for the whole site design.

Colors

Designer to choose colors to be used in the design.

```html
<!DOCTYPE html>
<html lang="en">
<head>
<meta charset="utf-8">
<title>Crafted Downriver — Home</title>
<link href="https://fonts.googleapis.com/css2?family=Ubuntu:wght@400;500;700&family=Arimo:wght@400;700&display=swap" rel="stylesheet">
<style>
:root{
  --red:#c8151b;
  --red-dark:#a50f14;
  --ink:#2a2a2a;
  --text:#444;
  --muted:#777;
  --topbar:#2b2b2b;
  --nav:#3a3a3a;
  --light:#ececec;
  --panel:#f6f6f6;
  --line:#d6d6d6;
  --white:#fff;
}
*{box-sizing:border-box;margin:0;padding:0}
html,body{width:801px;height:1200px;overflow:hidden}
body{position:relative;background:var(--white);font-family:"Arimo",Arial,sans-serif;color:var(--text)}
.abs{position:absolute}
svg{display:block}
/* top bar */
.topbar{left:0;top:0;width:801px;height:30px;background:var(--topbar);font-size:8px;color:#bbb;display:flex;justify-content:flex-end;align-items:center;gap:12px;padding-right:70px}
.topbar b{color:#fff;font-weight:400}
.topbar .mail{color:var(--red)}
/* header */
.header{left:0;top:30px;width:801px;height:114px;background:linear-gradient(#dcdcdc,#cfcfcf)}
.brand-mark{left:74px;top:40px;width:52px;height:52px;border-radius:50%;background:var(--red);border:3px solid #eee;box-shadow:0 0 0 1px #bbb}
.brand-name{left:134px;top:50px;font-family:"Ubuntu",sans-serif;font-weight:500;font-size:16px;line-height:19px;color:#555;text-transform:uppercase}
.helpdesk{right:94px;top:49px;font-family:"Ubuntu",sans-serif;font-weight:700;font-size:7.6px;color:#222;white-space:nowrap}
.phone-btn{left:712px;top:45px;width:15px;height:15px;background:var(--red);border-radius:3px;display:flex;align-items:center;justify-content:center}
.search{left:598px;top:72px;width:128px;height:12px;background:#e2e2e2;border-radius:3px;font-size:6px;color:#aaa;padding:2px 6px}
.search-btn{left:700px;top:72px;width:26px;height:12px;background:var(--red);border-radius:4px;display:flex;align-items:center;justify-content:center}
.nav{left:68px;top:98px;width:663px;height:35px;background:var(--nav);display:flex;align-items:center;padding-left:6px}
.nav a{font-family:"Ubuntu",sans-serif;font-weight:500;font-size:10px;color:#ddd;text-decoration:none;padding:0 11px;line-height:22px}
.nav a.active{background:var(--red);color:#fff;padding:0 15px}
.nav .social{margin-left:auto;display:flex;gap:3px;padding-right:10px}
.nav .social span{width:20px;height:20px;border-radius:50%;background:#555;border:1px solid #777;display:flex;align-items:center;justify-content:center}
/* slider */
.slider{left:0;top:150px;width:801px;height:280px;background:#1d2326}
.slide{left:65px;top:170px;width:666px;height:252px;background:linear-gradient(90deg,#4d5b62,#7a8a90 55%,#b9c2c5)}
.slide-photo{left:380px;top:170px;width:351px;height:252px;background:linear-gradient(90deg,rgba(0,0,0,0),rgba(40,40,40,.35))}
.slide-title{left:98px;top:232px;font-family:"Ubuntu",sans-serif;font-weight:500;color:#fff;font-size:20px;line-height:18px;text-transform:uppercase}
.slide-title em{font-style:normal;color:var(--red);font-size:28px;font-weight:700;display:block;line-height:26px}
.slide-copy{left:98px;top:303px;width:240px;font-size:6.4px;line-height:10.5px;color:#fff;font-weight:700;text-transform:uppercase}
.btn{background:var(--red);color:#fff;font-family:"Arimo",sans-serif;border-radius:3px;display:flex;align-items:center;justify-content:center;box-shadow:0 2px 2px rgba(0,0,0,.25)}
.slide-btn{left:98px;top:342px;width:90px;height:23px;font-size:8px;font-weight:700}
.arrow{font-family:"Ubuntu",sans-serif;color:#fff;font-size:34px;font-weight:700}
/* welcome */
.welcome{left:0;top:430px;width:801px;height:119px;background:var(--light)}
.welcome h1{position:absolute;left:69px;top:32px;font-family:"Ubuntu",sans-serif;font-weight:500;font-size:19px;color:var(--ink)}
.welcome h1 span{color:var(--red)}
.welcome p{position:absolute;left:69px;top:59px;width:340px;font-family:"Ubuntu",sans-serif;font-size:8.4px;line-height:11px;color:#555;white-space:nowrap;overflow:hidden}
.join{left:510px;top:484px;width:100px;height:26px;font-size:10px}
.learn{left:628px;top:484px;width:100px;height:24px;font-size:9px;font-weight:700}
/* news */
.news-head{left:0;top:549px;width:801px;height:53px;background:var(--white)}
.news-title{left:0;top:560px;width:746px;text-align:center;font-family:"Ubuntu",sans-serif;font-weight:500;font-size:16px;color:var(--ink)}
.news-title span{color:var(--red);font-weight:400}
.news-rule{top:570px;height:1px;background:var(--line)}
.news-nav{left:696px;top:577px;width:36px;height:25px;background:var(--red);color:#fff;font-size:14px;font-weight:700;display:flex;align-items:center;justify-content:center;gap:4px}
.news-band{left:0;top:602px;width:801px;height:240px;background:var(--light);border-top:1px solid var(--line)}
.card{top:625px;width:153px;height:199px;background:var(--panel);border:1px solid var(--line)}
.card.hot{background:var(--red);border-color:var(--red)}
.card-icon{top:-12px;left:62px;width:28px;height:28px;border-radius:50%;background:#3c3c3c;border:2px solid #fff;display:flex;align-items:center;justify-content:center}
.card-img{left:30px;top:15px;width:108px;height:100px;background:linear-gradient(#8fa1ad,#5c6a70)}
.card h3{position:absolute;left:24px;top:120px;width:116px;font-family:"Ubuntu",sans-serif;font-weight:500;font-size:9.6px;line-height:13px;color:#333;letter-spacing:.5px}
.card.hot h3{color:#fff}
.card .by{position:absolute;left:65px;top:167px;font-size:6.4px;line-height:10px;color:#555}
.card.hot .by{color:#fff;font-weight:700}
.card .more{position:absolute;left:14px;top:165px;width:40px;height:20px;font-size:6.4px}
.card.hot .more{background:#1f3a44}
/* featured */
.article{left:68px;top:853px;width:443px;height:175px;background:var(--panel);border:1px solid var(--line)}
.article h2{position:absolute;left:2px;top:7px;font-family:"Ubuntu",sans-serif;font-weight:400;font-size:17px;color:#333;letter-spacing:.5px}
.article h2 span{color:var(--red);font-weight:500}
.meta{position:absolute;left:2px;top:40px;width:437px;font-size:7px;color:#777;border-bottom:1px solid var(--line);padding-bottom:3px;white-space:nowrap}
.meta .r{color:var(--red)}
.meta u{color:#555}
.article p{position:absolute;left:2px;top:68px;width:262px;font-size:7px;line-height:13.2px;color:#333}
.read{position:absolute;left:3px;top:158px;font-size:6.4px;color:#777;letter-spacing:.5px}
.article-photo{left:350px;top:901px;width:139px;height:118px;background:linear-gradient(#d9d3c3,#7b7f86)}
.events{left:534px;top:855px;width:179px;height:175px;background:linear-gradient(#f2f4f6,#dfe4ea)}
.events-bar{left:534px;top:960px;width:179px;height:70px;background:#2a2e3f}
.events-logo{left:538px;top:965px;width:84px;height:59px;background:#fff;display:flex;align-items:center;justify-content:center;font-family:"Ubuntu",sans-serif;font-weight:500;font-size:7.5px;color:var(--red);text-transform:uppercase;text-align:center;line-height:9px}
.events-title{left:628px;top:972px;font-family:"Ubuntu",sans-serif;font-size:13px;line-height:17px;color:#fff}
.events-title span{color:var(--red);font-size:16px}
.events-link{left:630px;top:1016px;font-size:6px;color:#fff}
/* partners */
.footer{left:0;top:1076px;width:801px;height:124px;background:var(--red)}
.partners{left:71px;top:1058px;width:647px;height:65px;background:linear-gradient(#f2f2f2,#dedede);border-radius:6px;box-shadow:0 1px 3px rgba(0,0,0,.3)}
.badge{top:1078px;width:82px;height:20px;background:#8e8e8e;border-radius:4px}
.p-arrow{top:1074px;font-size:26px;color:#333;font-family:"Ubuntu",sans-serif}
.foot-mark{left:86px;top:1136px;width:54px;height:54px;border-radius:50%;background:var(--red);border:4px solid #eee}
.foot-links{left:200px;top:1150px;width:328px;text-align:center;font-size:7.2px;line-height:12.5px;color:#fff}
.foot-social{left:563px;top:1140px;display:flex;gap:7px}
.foot-social span{width:24px;height:24px;border-radius:50%;background:#e0474c;border:1px solid #f07070;display:flex;align-items:center;justify-content:center}
</style>
</head>
<body>

<div class="abs topbar"><span>Telephone: <b>+1 555 010 4410</b></span><span>FAX: <b>+1 555 010 4411</b></span><span class="mail">E-mail: hello@crafteddownriver.com</span></div>

<header class="abs header"></header>
<div class="abs brand-mark"></div>
<div class="abs brand-name">Crafted<br>Downriver</div>
<div class="abs helpdesk">HELP DESK 1-800-555-0142</div>
<div class="abs phone-btn"><svg width="9" height="9" viewBox="0 0 10 10"><path d="M2 1 L4 1 L4.6 3.2 L3.4 4 Q4.2 5.8 6 6.6 L6.8 5.4 L9 6 L9 8 Q9 9 8 9 Q1 8.5 1 2 Q1 1 2 1Z" fill="#fff"/></svg></div>
<div class="abs search">search</div>
<div class="abs search-btn"><svg width="8" height="8" viewBox="0 0 10 10"><circle cx="4" cy="4" r="2.8" fill="none" stroke="#fff" stroke-width="1.5"/><path d="M6 6 L9 9" stroke="#fff" stroke-width="1.8"/></svg></div>
<nav class="abs nav">
  <a class="active" href="#">Home</a><a href="#">Learn More</a><a href="#">News</a><a href="#">Events</a><a href="#">Members</a><a href="#">Council</a><a href="#">Annual Expo</a><a href="#">Awards</a>
  <div class="social"><span></span><span></span><span><svg width="10" height="8" viewBox="0 0 10 8"><rect x=".5" y=".5" width="9" height="7" fill="none" stroke="#fff"/><path d="M.5 .5 L5 4.5 L9.5 .5" fill="none" stroke="#fff"/></svg></span><span></span></div>
</nav>

<section class="abs slider"></section>
<div class="abs slide"></div>
<div class="abs slide-photo" role="img" aria-label="Portrait of a businessman in a dark suit"></div>
<div class="abs slide-title"><em>Strategies</em>That drive business<br>results</div>
<div class="abs slide-copy">Phasellus porta. Fusce susct varius mi. Cum sociis natquepenabus et dis parturient montes, nascetur ridiculus musnulla dui. Fusce feugiamalesuada odio.</div>
<div class="abs btn slide-btn">READ MORE</div>
<div class="abs arrow" style="left:22px;top:274px">&#8249;</div>
<div class="abs arrow" style="left:758px;top:274px">&#8250;</div>

<section class="abs welcome">
  <h1>Welcome to <span>Bright</span>mark Co!</h1>
  <p>At vero eos et accusamus et iusto odio dignissimos ducimus qui blanditiis praesent<br>molestias excepturi sint occaecati cupiditate non provident, similique sunt in culp</p>
</section>
<div class="abs btn join">Join Us</div>
<div class="abs btn learn">LEARN MORE</div>

<section class="abs news-head"></section>
<div class="abs news-rule" style="left:0;width:310px"></div>
<div class="abs news-rule" style="left:436px;width:365px"></div>
<div class="abs news-title">Latest <span>News</span></div>
<div class="abs news-nav"><span>&#8249;</span><span>&#8250;</span></div>
<section class="abs news-band"></section>

<article class="abs card" style="left:67px">
  <div class="abs card-icon"><svg width="12" height="14" viewBox="0 0 12 14"><rect x="1" y="1" width="10" height="12" rx="1" fill="none" stroke="#fff" stroke-width="1.2"/><rect x="3" y="3" width="6" height="2" fill="#fff"/><g fill="#fff"><rect x="3" y="7" width="1.6" height="1.4"/><rect x="5.2" y="7" width="1.6" height="1.4"/><rect x="7.4" y="7" width="1.6" height="1.4"/><rect x="3" y="9.6" width="1.6" height="1.4"/><rect x="5.2" y="9.6" width="1.6" height="1.4"/><rect x="7.4" y="9.6" width="1.6" height="1.4"/></g></svg></div>
  <div class="abs card-img" style="left:8px;width:138px;height:40px;background:#fff;display:flex;align-items:center;justify-content:center;font-family:Ubuntu,sans-serif;font-weight:500;font-size:10px;color:#1a9ad6">Linden Circuit Works</div>
  <h3 style="left:12px;top:60px;width:134px">Linden Circuit Works launch new website</h3>
  <div class="by" style="left:12px;top:110px">By:Linden<br>Circuit Works Ltd</div>
  <div class="btn more" style="left:14px;top:165px">MORE</div>
</article>
<article class="abs card" style="left:238px">
  <div class="abs card-icon"><svg width="13" height="13" viewBox="0 0 13 13"><g fill="#fff"><rect x="2" y="5" width="2.2" height="6"/><rect x="5.4" y="2" width="2.2" height="9"/><rect x="8.8" y="7" width="2.2" height="4"/><rect x="1" y="11.4" width="11" height="1"/></g></svg></div>
  <div class="abs card-img" style="left:24px;width:108px;background:linear-gradient(#9fb4c8,#6d6a66)" role="img" aria-label="Modern office building exterior"></div>
  <h3>Riverside Powder Finish help revamp sign for local theatre</h3>
  <div class="btn more">MORE</div>
  <div class="by">By:Linden<br>Circuit Works Ltd</div>
</article>
<article class="abs card hot" style="left:409px">
  <div class="abs card-icon"><svg width="12" height="14" viewBox="0 0 12 14"><path d="M4 1 L8 1 L7 3.5 Q11 6 11 10 Q11 13 6 13 Q1 13 1 10 Q1 6 5 3.5Z" fill="#fff"/><path d="M7.3 7 Q6 6.2 5 6.9 Q4.3 7.8 6 8.4 Q7.8 9 7 10.2 Q6 11 4.6 10.2 M6 5.8 L6 11.2" fill="none" stroke="#3c3c3c" stroke-width=".9"/></svg></div>
  <div class="abs card-img" style="left:24px;width:102px;background:linear-gradient(#e6e6e6,#3a3a3a)" role="img" aria-label="Industrial powder-coated cylinders"></div>
  <h3 style="top:118px">Riverside Powder Finish help revamp sign for local theatre</h3>
  <div class="btn more">MORE</div>
  <div class="by">By:Linden<br>Circuit Works Ltd</div>
</article>
<article class="abs card" style="left:579px">
  <div class="abs card-icon"><svg width="14" height="14" viewBox="0 0 14 14"><circle cx="7" cy="7" r="5.8" fill="none" stroke="#fff" stroke-width="1.2"/><path d="M7 3.5 L7 7 L9.6 8.6" fill="none" stroke="#fff" stroke-width="1.2"/></svg></div>
  <div class="abs card-img" style="left:28px;width:100px;background:linear-gradient(90deg,#8c97a0,#c4ccd2 60%,#2a5a9c 65%,#1f4a8a)" role="img" aria-label="Steel panel with blue coated surface"></div>
  <h3 style="top:118px">Riverside Powder Finish help revamp sign for local theatre</h3>
  <div class="btn more">MORE</div>
  <div class="by">By:Linden<br>Circuit Works Ltd</div>
</article>

<article class="abs article">
  <h2>FEATURED <span>ARTICLE</span></h2>
  <div class="meta"><span class="r">July 14, 2011</span> &nbsp;&nbsp;&nbsp;&nbsp; By <b>admin</b> &nbsp;&nbsp;&nbsp;&nbsp; Posted in <span class="r">Sit voluptatem, Totam rem, Ullam corporis</span> &nbsp;&nbsp;&nbsp;&nbsp; With <u>3 Comments</u></div>
  <p>Lorem ipsum dolor sit amet, consectetur adipiscing elit. Ut a metus diam, sit amet tristique risus. Aliquam dictum, lectus vel consequat malesuada, enim metus blandit urna, Lorem ipsum dolor sit amet, consectetur adipiscing elit. Ut a metus diam, sit amet tristique risus. Aliquam dictum, lectus vel consequat malesuada, enim metus blandit urna, vel sodales tellus nibh eget tortor.</p>
  <div class="read">READ MORE</div>
</article>
<div class="abs article-photo" role="img" aria-label="Two businessmen standing in front of an exhibition banner"></div>

<div class="abs events" role="img" aria-label="Hands applauding"></div>
<div class="abs events-bar"></div>
<div class="abs events-logo">Crafted<br>Downriver</div>
<div class="abs events-title">UPCOMING<br><span>EVENTS</span></div>
<div class="abs events-link">CLICK HERE &gt;&gt;</div>

<footer class="abs footer"></footer>
<div class="abs partners"></div>
<div class="abs p-arrow" style="left:80px">&#8249;</div>
<div class="abs p-arrow" style="left:697px">&#8250;</div>
<div class="abs badge" style="left:118px"></div>
<div class="abs badge" style="left:206px"></div>
<div class="abs badge" style="left:304px"></div>
<div class="abs badge" style="left:411px"></div>
<div class="abs badge" style="left:511px"></div>
<div class="abs badge" style="left:593px"></div>
<div class="abs foot-mark"></div>
<div class="abs foot-links">Home &nbsp; | &nbsp; Clients &nbsp; | &nbsp; awards &nbsp; | &nbsp; Members &nbsp; | &nbsp; More...<br>Copyright (C) crafted downriver 2014. All Rights Reserved</div>
<div class="abs foot-social"><span></span><span></span><span><svg width="11" height="11" viewBox="0 0 11 11"><circle cx="2" cy="9" r="1.3" fill="#fff"/><path d="M1 5.2 A4.8 4.8 0 0 1 5.8 10 M1 1.6 A8.4 8.4 0 0 1 9.4 10" fill="none" stroke="#fff" stroke-width="1.5"/></svg></span><span></span></div>

</body>
</html>
```